Advertisiment for children's classes and activities

We are a children's creative arts studio running classes and activities for children on a weekly bases. I am looking to design an ad that will promote our studio as a whole centre, offering specific classes for kids in the areas of art, music, and construction.

Target Market(s)

Parents of children (aged 4 to 12 years). The ad will be in a families magazine.

Industry/Entity Type

Construction

Requirements
Must have
• Size is 87mm wide x 60mm high

Our Logo / details
Address: 312-314 North Wattle Rd, Merrilee Vale, 4051
Phone: 07 3621 9047
email: info@bluewrenateliers.com.au
web: www.bluewrenateliers.com.au

Should be bright and colourful, in colours that match those in our logo.

Look fun, and include the line 'Classes, Workshops, and Activities for Kids'

Be obvious that we run kids classes and activities, either mentioning the specific programs or not.
Nice to have
• Include the text
Tunetoddle
Art Classes
Wren Bricks Classes
Holiday Workshops
Should not have
• A very young child focus. Although our market covers young children as well, it needs to look appropriate for older children.

```html
<!DOCTYPE html>
<html lang="en">
<head>
<meta charset="utf-8">
<title>Blue Wren Ateliers – Kids Classes Ad</title>
<link rel="stylesheet" href="https://fonts.googleapis.com/css2?family=Arvo:wght@400;700&family=Arimo:wght@400;700&display=swap">
<style>
  :root {
    --paper: #ffffff;
    --ribbon: #fbf6e2;
    --green: #3cb14a;
    --red: #e52d2d;
    --chalk-green: #3fae5a;
    --chalk-orange: #f08a4b;
    --chalk-blue: #3fb4dd;
    --chalk-pink: #e8368f;
    --brand-red: #e31e25;
    --caption: #1a1a1a;
    --sky-top: #d9e9f4;
    --sky-mid: #c9b49a;
    --skin: #e2b48e;
  }
  * { margin: 0; padding: 0; box-sizing: border-box; }
  html, body { width: 1200px; height: 727px; overflow: hidden; background: var(--paper); }
  .canvas { position: relative; width: 1200px; height: 727px; }
  .shapes { position: absolute; left: 0; top: 0; }
  .txt { position: absolute; white-space: nowrap; }
  .chalk { font-family: "Arvo", Georgia, serif; font-weight: 700; letter-spacing: 0.5px; }
  .tagline { font-family: "Arvo", Georgia, serif; font-weight: 700; color: var(--chalk-pink); font-size: 15px; }
  .contact { font-family: "Arimo", Arial, sans-serif; font-weight: 700; color: #fff; }
  .brand-name { font-family: "Arvo", Georgia, serif; font-weight: 700; color: var(--brand-red); text-align: center; line-height: 1.05; }
  .caption { font-family: "Arimo", Arial, sans-serif; font-size: 33px; color: var(--caption); }
  .green { color: var(--chalk-green); }
  .orange { color: var(--chalk-orange); }
  .blue { color: var(--chalk-blue); }
  .ink { color: #333; }

  /* landscape ad */
  .land-headline { left: 30px; top: 454px; font-size: 39px; }
  .land-tagline { left: 32px; top: 506px; }
  .land-programs { left: 32px; top: 520px; font-size: 31px; }
  .land-contact { left: 32px; top: 576px; font-size: 17px; line-height: 19.5px; }
  .land-brand { left: 480px; top: 560px; width: 170px; font-size: 27px; }

  /* portrait ad */
  .port-headline-1 { left: 752px; top: 298px; font-size: 31px; }
  .port-headline-2 { left: 838px; top: 324px; font-size: 31px; }
  .port-tagline { left: 780px; top: 372px; line-height: 20px; text-align: center; }
  .port-programs-1 { left: 752px; top: 416px; font-size: 31px; }
  .port-programs-2 { left: 784px; top: 442px; font-size: 31px; }
  .port-contact { left: 756px; top: 500px; font-size: 19px; line-height: 22px; }
  .port-web { left: 743px; top: 605px; width: 450px; font-size: 19px; line-height: 22px; text-align: center; }
  .port-brand { left: 1040px; top: 505px; width: 150px; font-size: 24px; }

  .caption-land { left: 22px; top: 680px; }
  .caption-port { left: 752px; top: 680px; }
</style>
</head>
<body>
<main class="canvas">
  <svg class="shapes" width="1200" height="727" viewBox="0 0 1200 727" aria-hidden="false">
    <defs>
      <linearGradient id="kids-photo" x1="0" y1="0" x2="0" y2="1">
        <stop offset="0" stop-color="var(--sky-top)"/>
        <stop offset="0.55" stop-color="var(--sky-mid)"/>
        <stop offset="1" stop-color="var(--skin)"/>
      </linearGradient>
      <clipPath id="clip-land"><rect x="18" y="218" width="652" height="450"/></clipPath>
      <clipPath id="clip-port"><rect x="743" y="8" width="450" height="652"/></clipPath>
    </defs>

    <!-- landscape ad -->
    <g class="ad-landscape" clip-path="url(#clip-land)">
      <rect x="18" y="218" width="652" height="360" fill="url(#kids-photo)" role="img" aria-label="Photo of smiling children leaning in toward the camera against a blue sky"/>
      <rect x="18" y="570" width="520" height="98" fill="var(--green)"/>
      <circle cx="600" cy="575" r="175" fill="var(--paper)"/>
      <polygon points="18,455 470,452 492,478 476,502 496,530 470,562 18,562" fill="var(--ribbon)"/>
    </g>

    <!-- portrait ad -->
    <g class="ad-portrait" clip-path="url(#clip-port)">
      <rect x="743" y="8" width="450" height="500" fill="url(#kids-photo)" role="img" aria-label="Photo of smiling children leaning in toward the camera against a blue sky"/>
      <rect x="743" y="490" width="310" height="110" fill="var(--green)"/>
      <circle cx="1120" cy="485" r="132" fill="var(--paper)"/>
      <polygon points="743,300 1010,286 992,318 1014,345 994,374 1010,402 743,408" fill="var(--ribbon)"/>
      <polygon points="743,416 1012,414 995,440 1014,462 996,486 743,488" fill="var(--ribbon)"/>
      <rect x="743" y="600" width="450" height="60" fill="var(--red)"/>
    </g>
  </svg>

  <!-- landscape ad text -->
  <div class="txt chalk land-headline"><span class="green">Life</span> <span class="orange">lived</span> <span class="blue">creatively</span></div>
  <div class="txt tagline land-tagline">Classes, Workshops,and Activities for Kids</div>
  <div class="txt chalk land-programs"><span class="green">art</span><span class="ink">,</span> <span class="blue">music</span><span class="ink">,</span> <span class="orange">construction</span></div>
  <div class="txt contact land-contact">
    Address: 312-314 North Wattle Rd,<br>
    Merrilee Vale, 4051 / Phone: 07 3621 9047<br>
    email: info@bluewrenateliers.com.au<br>
    web: www.bluewrenateliers.com.au
  </div>
  <div class="txt brand-name land-brand">Blue Wren<br>Ateliers</div>

  <!-- portrait ad text -->
  <div class="txt chalk port-headline-1"><span class="green">Life</span> <span class="orange">lived</span></div>
  <div class="txt chalk port-headline-2"><span class="blue">creatively</span></div>
  <div class="txt tagline port-tagline">Classes, Workshops,<br>and Activities for Kids</div>
  <div class="txt chalk port-programs-1"><span class="green">art</span><span class="ink">,</span> <span class="blue">music</span><span class="ink">,</span></div>
  <div class="txt chalk port-programs-2"><span class="orange">construction</span></div>
  <div class="txt contact port-contact">
    Address: 312-314<br>
    North Wattle Rd,<br>
    Merrilee Vale, 4051<br>
    Phone: 07 3621 9047
  </div>
  <div class="txt contact port-web">
    info@bluewrenateliers.com.au<br>
    www.bluewrenateliers.com.au
  </div>
  <div class="txt brand-name port-brand">Blue Wren<br>Ateliers</div>

  <!-- size captions -->
  <div class="txt caption caption-land">87mm wide and 60mm</div>
  <div class="txt caption caption-port">60mm wide and 87mm</div>
</main>
</body>
</html>
```